Flyer Design Project - law firm

I need a design for an advertising flyer for my law firm.
Ideally the size of the document will be one page A4.
I have attached a copy of the logo. I would like the lettering for 'Dornwick Legal' to be all the same size, rather than the 'S' and 'L' being slightly larger
The flyer must include the text below:
Wills
Anyone who owns property or investments or has family obligations should have a Will to ensure that their assets are distributed in accordance with their wishes and that their children are cared for by the guardians of their choosing. Without a Will, these vital decisions are determined by the government or the courts of the State or Territory which you lived in at the time of your death.
Dornwick Legal can assist you in the preparation of a legal will tailored to your particular circumstances to ensure that your wishes are followed.
We are offering Halbrook- Crestmere clients a free discussion of their will requirements and a heavily discounted standard wills package of
$330.00* for a single will
$550.00* for couples wills
These prices are only valid prior to your conveyancing settlement for standard wills (e.g. not including a testamentary trust or other complications.
Please contact us on or provide Halbrook Crestmere with authority for us to contact you today.
Updates
Hi All,
I have posted a copy of the proposed logo. Please note that I need the wording of 'Dornwick Legal' to all be the same size, rather than the 'S' and 'L' being slightly larger.
If you require anything further please let me know.
Thanks
I have added copies of the logo in ups format,
If you require anything further please let know.
Thanks for your assistance.
Industry/Entity Type
Advertising
Look and feel
Each slider illustrates characteristics of the customer's brand and the style your logo design should communicate.

```html
<!DOCTYPE html>
<html lang="en">
<head>
<meta charset="utf-8">
<title>Dornwick Legal – Wills</title>
<link href="https://fonts.googleapis.com/css2?family=Old+Standard+TT&family=Open+Sans:ital,wght@0,400;1,400&display=swap" rel="stylesheet">
<style>
  :root {
    --ink: #1a1a1a;
    --paper: #ffffff;
    --crimson: #b8324a;
    --maroon: #2a0606;
    --wine: #5a1212;
    --gold: #f3b41c;
    --amber: #c9861a;
    --pink: #e4508a;
    --yellow: #f6e63a;
    --black: #000000;
    --box-line: rgba(255, 255, 255, 0.45);
  }
  * { margin: 0; padding: 0; box-sizing: border-box; }
  html, body { width: 848px; height: 1200px; overflow: hidden; background: var(--paper); }
  .flyer {
    position: relative;
    width: 848px;
    height: 1200px;
    background: var(--paper);
    color: var(--ink);
    font-family: "Open Sans", Arial, sans-serif;
  }
  .hero-photo {
    position: absolute; left: 0; top: 0; width: 848px; height: 362px;
    background:
      radial-gradient(ellipse at 75% 25%, rgba(246, 210, 110, 0.95) 0%, rgba(214, 150, 50, 0.7) 30%, transparent 60%),
      radial-gradient(ellipse at 35% 55%, rgba(70, 20, 12, 0.9) 0%, transparent 55%),
      linear-gradient(90deg, #b8404a 0%, #8a2a22 30%, #5a2414 55%, #b07a2a 80%, #d9a44a 100%);
  }
  .firm-name {
    position: absolute; left: 0; top: 372px; width: 848px;
    text-align: center;
    font-family: "Old Standard TT", Georgia, serif;
    font-size: 66px; font-weight: 400; line-height: 1;
    color: var(--ink);
  }
  .service {
    position: absolute; left: 0; top: 464px; width: 848px;
    text-align: center; font-size: 22px; line-height: 1.2;
  }
  .copy {
    position: absolute; left: 44px; width: 760px;
    text-align: center; font-size: 16.4px; line-height: 23px;
  }
  .copy-intro { top: 499px; }
  .copy-assist { top: 681px; }
  .copy-offer { top: 809px; }
  .price-band {
    position: absolute; left: 0; top: 866px; width: 848px; height: 100px;
    background: linear-gradient(90deg, var(--crimson) 0%, var(--wine) 25%, var(--maroon) 50%, #4a2008 65%, var(--amber) 85%, var(--gold) 100%);
  }
  .price-box {
    position: absolute; top: 12px; width: 311px; height: 78px;
    border: 1px solid var(--box-line); border-radius: 12px;
    background: rgba(0, 0, 0, 0.18);
    color: var(--paper); text-align: center;
    font-family: "Old Standard TT", Georgia, serif;
  }
  .price-box.couple { left: 52px; }
  .price-box.single { left: 477px; }
  .price-amount { display: block; font-size: 31px; line-height: 1; margin-top: 7px; }
  .price-label { display: block; font-size: 24px; line-height: 1.1; margin-top: 2px; }
  .terms {
    position: absolute; left: 42px; top: 994px; width: 780px;
    font-style: italic; font-size: 16px; line-height: 23px;
  }
  .footer-art {
    position: absolute; left: 0; top: 1068px; width: 848px; height: 100px;
    background: linear-gradient(90deg, var(--pink) 0%, #c23a5e 30%, #7a2a22 55%, #e0b020 75%, var(--yellow) 100%);
  }
  .footer-bar {
    position: absolute; left: 0; top: 1168px; width: 848px; height: 32px;
    background: var(--black);
  }
</style>
</head>
<body>
  <main class="flyer">
    <div class="hero-photo" role="img" aria-label="Photograph of a judge's gavel in front of an open law book, with binary digits overlaid in warm red and gold tones"></div>

    <h1 class="firm-name">dornwick legal</h1>
    <h2 class="service">Wills</h2>

    <p class="copy copy-intro">Anyone who owns property or investments or has family obligations should have a Will to ensure that their assets are distributed in accordance with their wishes and that their children are cared for by the guardians of their choosing. Without a Will, these vital decisions are determined by the government or the courts of the State or Territory which you lived in at the time of your death.</p>

    <p class="copy copy-assist" style="top:600px">Dornwick Legal can assist you in the preparation of a legal will tailored to your particular circumstances to ensure that your wishes are followed.</p>

    <p class="copy copy-offer" style="top:700px">We are offering Halbrook Crestmere clients a free discussion of their will requirements and a heavily discounted standard wills package of</p>

    <section class="price-band">
      <div class="price-box couple">
        <span class="price-amount">$550.00*</span>
        <span class="price-label">for couples wills</span>
      </div>
      <div class="price-box single">
        <span class="price-amount">$330.00*</span>
        <span class="price-label">for sngle will</span>
      </div>
    </section>

    <p class="terms">These prices are only valid prior to your conveyancing settlement for standard wills (e.g. not including a testamentary trust or other complications.</p>

    <div class="footer-art" role="img" aria-label="Stylised three-dimensional lettering reading THE LAW in pink and yellow tones"></div>
    <div class="footer-bar"></div>
  </main>
</body>
</html>
```